Create a banner for me that embodies my health and well being package.

I am an intuitive counselor with a busy practice helping clients to shift their blocks and move forward in their lives.
I have created a package called '9 paths home again'
I am wanting a banner to put on my website page, facebook page and to use as a letter head in mailouts.
My ideal clients are those who want to create change in their lives and who invest money in themselves and their personal and spiritual growth.
I am different to regular life coaches as my sessions have a spiritual twist to them creating much deeper change in my clients.
I would like the banner to be mainly font with the title of the progam: 9 Paths Home Again (no other wording) (something along the lines of the Blackjack font) and that ties in with the theme of my website. I'm not sure what else I want with it and am looking for ideas.
Website:
www.quillorabalancecare.com.au
I also have a current facebook page for the business:
https://www.facebook.com/Quillora-Balance-Care-402715938846102/
(Note: I am about to drop my logo and business name and move to using my own name - the rest of the website will remain the same).
I have attached a doc with the draft of what wording will be on the website page any advertising will link to, to give you an idea of what the program is about.

Target Market(s)

People who invest money on themselves who are looking to improve their emotional well being and creating change in their life. Majority are middle aged women (also younger females and some men)

Industry/Entity Type

Health And Wellness

Font styles to use
Other font styles liked:
• I like Blackjack and Amienne. Along those lines.

Requirements
Must have
• Attractive, modern and GREAT font.
Nice to have
• Surprise me with something amazing!
• I love the colours in the 2 images I have up loaded as they represent the heart chakra colours. They could be a feature on the banner or blurred into the background.
Should not have
• Even though my work is quite spiritual I don't want it to look woo woo (meaning airy fairy spiritual stuff!)

```html
<!DOCTYPE html>
<html lang="en">
<head>
<meta charset="utf-8">
<title>9 Paths Home Again – Banner</title>
<link rel="stylesheet" href="https://fonts.googleapis.com/css2?family=Dancing+Script:wght@500&display=swap">
<style>
  :root {
    --paper-light: #fbfbfb;
    --paper-mid: #ececec;
    --paper-shadow: #d9d9d9;
    --heart-green: #2f8a3c;
  }
  html, body {
    margin: 0;
    padding: 0;
    overflow: hidden;
    background: #ffffff;
  }
  .banner {
    position: relative;
    width: 1200px;
    height: 444px;
    overflow: hidden;
  }
  .banner__paper {
    position: absolute;
    inset: 0;
    background:
      radial-gradient(ellipse at 30% 40%, var(--paper-light) 0%, transparent 55%),
      radial-gradient(ellipse at 75% 65%, var(--paper-light) 0%, transparent 50%),
      linear-gradient(135deg, var(--paper-mid) 0%, var(--paper-light) 35%, var(--paper-shadow) 60%, var(--paper-light) 80%, var(--paper-mid) 100%);
  }
  .banner__content {
    position: absolute;
    inset: 0;
    display: flex;
    align-items: center;
    justify-content: center;
    color: var(--heart-green);
  }
  .banner__title {
    margin: 0 0 24px;
    font-family: "Dancing Script", cursive;
    font-weight: 500;
    font-size: 82px;
    line-height: 1.2;
    text-align: center;
  }
</style>
</head>
<body>
  <div class="banner">
    <div class="banner__paper" role="img" aria-label="Crumpled white paper texture background"></div>
    <div class="banner__content">
      <h1 class="banner__title">9 paths home again</h1>
    </div>
  </div>
</body>
</html>
```